DJ business brochure

I need a business brochure for my DJ business. Something that represents my business being owned and operated by first responders yet elegant enough to attract customers for weddings.

I do not have a preference on a type of brochure. Tri-fold or standard. The front page should have our logo and the name of our company. Under the name of our company it should say "Owned and operated by First Responders"

Bullet points for the brochure
LED up lighting.
Video projection
Dancing in the clouds
Top rated and experienced DJ's
Fun, crowd interactive DJ's
Text song request line.
Professional reception planning.

It should say somewhere on the brochure "When you choose Ember Deck you become part of the first responder family."

Contact information Rob@emberdeckdj.net Phone or text (738) 261-4907

Please use some fun pictures of weddings or people dancing. Does not specifically need to be from our sites.

Target Market(s)

Brides/Groom

Industry/Entity Type

Wedding/Party DJ

Requirements
Must have
• I want the wow factor. Something that when people look at the brochure they are drawn to read it. Email Rob@EmberDeckDJ.net Phone (738) 261-4907
Nice to have
• Nice to have a flaming vinyl record or a flaming musical note somewhere in the brochure.

```html
<!DOCTYPE html>
<html lang="en">
<head>
<meta charset="utf-8">
<title>Ember Deck – DJ Brochure</title>
<link rel="stylesheet" href="https://fonts.googleapis.com/css2?family=Audiowide&family=Montserrat:wght@400;500;600&family=Roboto+Condensed:wght@700&family=Roboto+Slab:wght@400;600;700&display=swap">
<style>
  :root{
    --page:#e9e6e3;
    --ink:#0e0a0c;
    --white:#ffffff;
    --ring-grey:#7b7a7d;
    --ring-light:#c9c9cc;
    --red:#d0142c;
    --red-deep:#a3101f;
    --maroon:#5a1228;
    --maroon-dark:#3a0b1b;
    --muted:#d9d2d4;
    --label:#cfcfd2;
  }
  html,body{margin:0;padding:0;width:1200px;height:1200px;overflow:hidden;background:var(--page);}
  .canvas{position:relative;width:1200px;height:1200px;}
  .spread{position:absolute;left:230px;width:740px;height:571px;display:block;box-shadow:0 6px 18px rgba(0,0,0,.25);}
  .spread--outside{top:19px;}
  .spread--inside{top:610px;}
  .intro{font-family:"Roboto Slab",serif;font-weight:600;font-size:16px;fill:var(--white);}
  .contact-label{font-family:"Roboto Condensed",sans-serif;font-weight:700;font-size:19px;fill:var(--label);}
  .contact-line{font-family:"Montserrat",sans-serif;font-weight:500;font-size:19px;fill:var(--white);}
  .contact-small{font-family:"Montserrat",sans-serif;font-size:14px;fill:var(--white);}
  .web{font-family:"Montserrat",sans-serif;font-size:18px;fill:var(--white);}
  .brand-name{font-family:"Montserrat",sans-serif;font-weight:600;fill:var(--white);}
  .tagline{font-family:"Audiowide",sans-serif;font-size:29px;fill:var(--red);stroke:var(--white);stroke-width:1.3px;paint-order:stroke;letter-spacing:1px;}
  .quote{font-family:"Roboto Slab",serif;font-weight:600;font-size:17px;fill:var(--white);}
  .quote-mark{font-family:"Roboto Slab",serif;font-weight:700;font-size:46px;fill:var(--white);}
  .services-title{font-family:"Roboto Slab",serif;font-weight:700;font-size:31px;fill:var(--muted);}
  .service{font-family:"Roboto Slab",serif;font-size:17px;fill:var(--muted);}
  .ring-outer{fill:none;stroke:var(--white);stroke-width:3;}
  .ring{fill:none;stroke:var(--ring-grey);stroke-width:9;}
  .band{fill:none;stroke:var(--ring-light);stroke-width:10;}
</style>
</head>
<body>
<div class="canvas">

  <!-- Outside spread: intro, contact, cover -->
  <svg class="spread spread--outside" viewBox="0 0 1085 837" xmlns="http://www.w3.org/2000/svg">
    <defs>
      <linearGradient id="tentScene" x1="0" y1="0" x2="1" y2="1">
        <stop offset="0" stop-color="#2a2140"/>
        <stop offset=".45" stop-color="#5b4a6e"/>
        <stop offset="1" stop-color="#2e2a22"/>
      </linearGradient>
      <linearGradient id="danceScene" x1="0" y1="0" x2="1" y2="1">
        <stop offset="0" stop-color="#cfc6dc"/>
        <stop offset=".4" stop-color="#6b5660"/>
        <stop offset=".75" stop-color="#8a2a32"/>
        <stop offset="1" stop-color="#3a2a2a"/>
      </linearGradient>
      <linearGradient id="deckScene" x1="0" y1="0" x2="0" y2="1">
        <stop offset="0" stop-color="#c9a3b8"/>
        <stop offset=".45" stop-color="#3a2432"/>
        <stop offset="1" stop-color="#0d1430"/>
      </linearGradient>
      <linearGradient id="fadeDark" x1="0" y1="0" x2="0" y2="1">
        <stop offset="0" stop-color="#0e0a0c" stop-opacity="0"/>
        <stop offset="1" stop-color="#0e0a0c"/>
      </linearGradient>
      <radialGradient id="circA" cx=".5" cy=".5" r=".6"><stop offset="0" stop-color="#b9a5c9"/><stop offset="1" stop-color="#3b3048"/></radialGradient>
      <radialGradient id="circB" cx=".5" cy=".5" r=".6"><stop offset="0" stop-color="#6f7fb0"/><stop offset="1" stop-color="#1b1c2e"/></radialGradient>
      <radialGradient id="circC" cx=".5" cy=".5" r=".6"><stop offset="0" stop-color="#d2307f"/><stop offset="1" stop-color="#4a1a6a"/></radialGradient>
    </defs>

    <rect width="1085" height="837" fill="var(--ink)"/>

    <g role="img" aria-label="Photo of an evening wedding reception under lit white tents">
      <path d="M0,230 C140,190 300,170 430,170 L720,200 L720,620 L0,620 Z" fill="url(#tentScene)"/>
      <rect x="430" y="420" width="295" height="220" fill="url(#fadeDark)"/>
    </g>
    <g role="img" aria-label="Photo of the bride dancing with guests in red dresses">
      <path d="M435,0 L1085,0 L1085,440 C980,470 850,450 720,440 C600,400 500,260 435,0 Z" fill="url(#danceScene)"/>
    </g>
    <rect x="725" y="470" width="360" height="367" fill="#120c0e"/>
    <rect x="430" y="560" width="295" height="277" fill="var(--ink)"/>

    <g role="img" aria-label="Photo of a DJ controller and laptop setup">
      <path d="M0,470 C210,440 390,580 430,837 L0,837 Z" fill="url(#deckScene)"/>
    </g>
    <path class="band" d="M0,468 C210,438 392,578 432,837"/>
    <path class="band" d="M435,0 C470,200 560,380 720,440 C850,470 980,470 1085,440"/>

    <g role="img" aria-label="Photo of guests dancing at a reception">
      <circle cx="456" cy="144" r="72" fill="url(#circA)"/>
    </g>
    <circle class="ring" cx="456" cy="144" r="76"/><circle class="ring-outer" cx="456" cy="144" r="84"/>

    <g role="img" aria-label="Photo of firefighters in helmets dancing with the bride">
      <circle cx="593" cy="337" r="92" fill="url(#circB)"/>
    </g>
    <circle class="ring" cx="593" cy="337" r="96"/><circle class="ring-outer" cx="593" cy="337" r="105"/>

    <g role="img" aria-label="Photo of guests dancing under pink lights">
      <circle cx="249" cy="490" r="80" fill="url(#circC)"/>
    </g>
    <circle class="ring" cx="249" cy="490" r="84"/><circle class="ring-outer" cx="249" cy="490" r="93"/>

    <text class="intro" x="38" y="52">
      <tspan x="38">Professional DJ / VJ services operated</tspan>
      <tspan x="38" dy="19">by first responders. Top rated for</tspan>
      <tspan x="38" dy="19">weddings. Exclusive discounts for</tspan>
      <tspan x="38" dy="19">public safety professionals.</tspan>
      <tspan x="38" dy="19">Call, text or email us for information</tspan>
      <tspan x="38" dy="19">and quotes.</tspan>
    </text>

    <!-- small brand mark -->
    <circle cx="555" cy="530" r="24" fill="none" stroke="var(--ring-light)" stroke-width="3"/>
    <text class="brand-name" x="555" y="588" text-anchor="middle" font-size="22">Ember Deck</text>

    <text class="contact-label" x="542" y="683" text-anchor="middle">CONTACT INFORMATION</text>
    <rect x="432" y="690" width="220" height="2" fill="var(--red)"/>
    <text class="contact-line" x="542" y="718" text-anchor="middle">Rob@emberdeckdj.net</text>
    <text class="contact-line" x="542" y="745" text-anchor="middle">(738) 261-4907</text>
    <text class="contact-small" x="542" y="763" text-anchor="middle">Phone or text</text>
    <text class="web" x="542" y="804" text-anchor="middle">www.EmberDeckDJ.net</text>

    <!-- cover -->
    <circle cx="905" cy="455" r="38" fill="none" stroke="var(--ring-light)" stroke-width="4"/>
    <text class="brand-name" x="905" y="560" text-anchor="middle" font-size="38">Ember Deck</text>
    <text class="tagline" x="905" y="648" text-anchor="middle">OWNED AND</text>
    <text class="tagline" x="905" y="683" text-anchor="middle">OPERATED</text>
    <text class="tagline" x="905" y="718" text-anchor="middle">BY FIRST</text>
    <text class="tagline" x="905" y="753" text-anchor="middle">RESPONDERS</text>
    <text class="web" x="905" y="804" text-anchor="middle">www.EmberDeckDJ.net</text>
  </svg>

  <!-- Inside spread: services and quote -->
  <svg class="spread spread--inside" viewBox="0 0 1085 837" xmlns="http://www.w3.org/2000/svg">
    <defs>
      <linearGradient id="partyScene" x1="0" y1="0" x2="1" y2="1">
        <stop offset="0" stop-color="#a05cc8"/>
        <stop offset=".35" stop-color="#5a3aa0"/>
        <stop offset=".6" stop-color="#3a2f8a"/>
        <stop offset=".8" stop-color="#c05a8a"/>
        <stop offset="1" stop-color="#e0a0c8"/>
      </linearGradient>
      <linearGradient id="servicePanel" x1="0" y1="0" x2="0" y2="1">
        <stop offset="0" stop-color="var(--maroon)"/>
        <stop offset="1" stop-color="var(--maroon-dark)"/>
      </linearGradient>
      <radialGradient id="c1" cx=".5" cy=".5" r=".6"><stop offset="0" stop-color="#7a60ff"/><stop offset="1" stop-color="#1c1670"/></radialGradient>
      <radialGradient id="c2" cx=".5" cy=".5" r=".6"><stop offset="0" stop-color="#d04a9a"/><stop offset="1" stop-color="#3a1ad0"/></radialGradient>
      <radialGradient id="c3" cx=".5" cy=".5" r=".6"><stop offset="0" stop-color="#b07a6a"/><stop offset="1" stop-color="#4a2a30"/></radialGradient>
      <radialGradient id="c4" cx=".5" cy=".5" r=".6"><stop offset="0" stop-color="#4aa0e0"/><stop offset="1" stop-color="#16284a"/></radialGradient>
      <radialGradient id="c5" cx=".5" cy=".5" r=".6"><stop offset="0" stop-color="#d04a70"/><stop offset="1" stop-color="#3a1a40"/></radialGradient>
    </defs>

    <g role="img" aria-label="Photo of a crowded dance floor at a wedding reception under colored lights">
      <rect width="1085" height="837" fill="url(#partyScene)"/>
    </g>
    <g role="img" aria-label="Photo of wedding guests dancing arm in arm">
      <path d="M0,0 L470,0 C490,200 430,330 230,400 C140,430 60,430 0,420 Z" fill="#b78bd6" opacity=".55"/>
    </g>

    <path d="M0,418 C120,432 230,420 320,440 C420,460 500,500 560,540 C490,630 448,730 433,837 L0,837 Z" fill="url(#servicePanel)"/>
    <path class="band" d="M470,0 C490,200 430,330 230,400 C140,430 60,430 0,420"/>
    <path class="band" d="M433,837 C445,700 520,580 631,456 C760,410 900,400 1085,415"/>

    <g role="img" aria-label="Photo of a couple's first dance in purple light"><circle cx="448" cy="212" r="97" fill="url(#c1)"/></g>
    <circle class="ring" cx="448" cy="212" r="101"/><circle class="ring-outer" cx="448" cy="212" r="110"/>

    <g role="img" aria-label="Photo of guests dancing under blue lights"><circle cx="168" cy="426" r="87" fill="url(#c2)"/></g>
    <circle class="ring" cx="168" cy="426" r="91"/><circle class="ring-outer" cx="168" cy="426" r="100"/>

    <g role="img" aria-label="Photo of guests dancing in a circle"><circle cx="631" cy="456" r="88" fill="url(#c3)"/></g>
    <circle class="ring" cx="631" cy="456" r="92"/><circle class="ring-outer" cx="631" cy="456" r="101"/>

    <g role="img" aria-label="Photo of a dance floor lit by stage lights"><circle cx="912" cy="401" r="100" fill="url(#c4)"/></g>
    <circle class="ring" cx="912" cy="401" r="104"/><circle class="ring-outer" cx="912" cy="401" r="114"/>

    <g role="img" aria-label="Photo of guests cheering on the dance floor"><circle cx="472" cy="670" r="80" fill="url(#c5)"/></g>
    <circle class="ring" cx="472" cy="670" r="84"/><circle class="ring-outer" cx="472" cy="670" r="93"/>

    <!-- quote -->
    <path d="M772,40 H1038 a8,8 0 0 1 8,8 V154 a8,8 0 0 1 -8,8 H975 L950,190 L948,162 H772 a8,8 0 0 1 -8,-8 V48 a8,8 0 0 1 8,-8 Z" fill="var(--red-deep)" opacity=".92"/>
    <text class="quote-mark" x="772" y="96">“</text>
    <text class="quote" x="790" y="96">
      <tspan x="790">When you choose Ember Deck</tspan>
      <tspan x="790" dy="21">you become part of the first</tspan>
      <tspan x="790" dy="21">responder family.</tspan>
    </text>
    <text class="quote-mark" x="1005" y="172">”</text>

    <!-- services -->
    <circle cx="60" cy="568" r="15" fill="var(--red)"/>
    <circle cx="60" cy="568" r="4" fill="var(--maroon)"/>
    <text class="services-title" x="93" y="581">DJ SERVICES</text>
    <rect x="40" y="593" width="282" height="1.5" fill="#8a3a4a"/>
    <g class="service-list">
      <circle cx="49" cy="610" r="7" fill="#b9b0b3"/><text class="service" x="64" y="616">LED up lighting.</text>
      <circle cx="49" cy="640" r="7" fill="#b9b0b3"/><text class="service" x="64" y="646">Video projection</text>
      <circle cx="49" cy="670" r="7" fill="#b9b0b3"/><text class="service" x="64" y="676">Dancing in the clouds</text>
      <circle cx="49" cy="700" r="7" fill="#b9b0b3"/><text class="service" x="64" y="706">Top rated and experienced DJ’s</text>
      <circle cx="49" cy="730" r="7" fill="#b9b0b3"/><text class="service" x="64" y="736">Fun, crowd interactive DJ’s</text>
      <circle cx="49" cy="760" r="7" fill="#b9b0b3"/><text class="service" x="64" y="766">Text song request line.</text>
      <circle cx="49" cy="790" r="7" fill="#b9b0b3"/><text class="service" x="64" y="796">Professional reception planning.</text>
    </g>
  </svg>

</div>
</body>
</html>
```